A Billboard Sign - TWO SIGNS

Hi, I’m looking to produce approximately 2.74 m by 2.74 m for a billboard-style display. I have a mock-up of the general look and feel, but I need a more polished, professional design. The sign will be viewed by people driving past, so the messaging must be clear, bold and easily readable at speed.

I also need a second sign sized 1 m by 3 m, following the same branding and visual style as the larger piece.

Requirements
Must have
• It must use the colours I've submitted
Nice to have
• I would like to see some good ideas in the general theme of what I have Mocked up. I don't the same design sent back to me

```html
<!DOCTYPE html>
<html lang="en">
<head>
<meta charset="utf-8">
<title>Brightwave Insights – Billboard Signs</title>
<link href="https://fonts.googleapis.com/css2?family=Montserrat:wght@600;700;800&display=swap" rel="stylesheet">
<style>
  :root {
    --brand-orange: #f7981d;
    --brand-navy: #1b2a35;
    --text-white: #ffffff;
    --stage-bg: #e8e5df;
    --frame-grey: #c9ced2;
  }
  * { margin: 0; padding: 0; box-sizing: border-box; }
  html, body {
    width: 1200px; height: 2444px; overflow: hidden;
    background: var(--stage-bg);
    font-family: "Montserrat", Arial, sans-serif;
  }
  .canvas { position: relative; width: 1200px; height: 2444px; }

  .sign { position: absolute; background: var(--brand-orange); overflow: hidden; }
  .brand { position: absolute; display: flex; align-items: center; color: var(--brand-navy); }
  .brand__dot { border-radius: 50%; background: var(--brand-navy); flex: none; }
  .brand__name { font-weight: 700; line-height: 1.05; letter-spacing: 0.04em; white-space: nowrap; }

  .headline { position: absolute; text-align: center; color: var(--brand-navy); }
  .headline__main { font-weight: 800; line-height: 1.02; letter-spacing: 0.01em; white-space: nowrap; }
  .headline__sub { font-weight: 800; letter-spacing: 0.01em; margin-top: 6px; white-space: nowrap; }

  .partner-band { position: absolute; left: 0; right: 0; bottom: 0; background: var(--brand-navy); color: var(--text-white); }
  .partner-band__label { position: absolute; font-weight: 800; letter-spacing: 0.02em; white-space: nowrap; }
  .partner { position: absolute; display: flex; align-items: center; font-weight: 700; color: var(--text-white); white-space: nowrap; }
  .partner--north { letter-spacing: 0.08em; }
  .partner__square { background: var(--text-white); flex: none; }
  .partner-band__web { position: absolute; text-align: center; font-weight: 800; letter-spacing: 0.03em; white-space: nowrap; }

  /* square sign, 2.74 m x 2.74 m */
  .sign--square { left: 106px; top: 150px; width: 988px; height: 916px; outline: 10px solid var(--frame-grey); }
  .sign--square .brand { left: 60px; top: 120px; gap: 46px; }
  .sign--square .brand__dot { width: 200px; height: 200px; }
  .sign--square .brand__name { font-size: 66px; }
  .sign--square .headline { left: 0; right: 0; top: 452px; }
  .sign--square .headline__main { font-size: 66px; }
  .sign--square .headline__sub { font-size: 36px; }
  .sign--square .partner-band { height: 184px; }
  .sign--square .partner-band__label { left: 28px; top: 16px; font-size: 18px; }
  .sign--square .partner--north { left: 100px; top: 66px; font-size: 40px; }
  .sign--square .partner--quad { left: 620px; top: 66px; font-size: 40px; gap: 16px; }
  .sign--square .partner__square { width: 50px; height: 50px; }
  .sign--square .partner-band__web { left: 0; right: 0; top: 142px; font-size: 18px; }

  /* wide sign, 3 m x 1 m */
  .sign--wide { left: 0; top: 1640px; width: 1200px; height: 400px; }
  .sign--wide .brand { left: 40px; top: 56px; gap: 26px; }
  .sign--wide .brand__dot { width: 160px; height: 160px; }
  .sign--wide .brand__name { font-size: 40px; }
  .sign--wide .headline { left: 540px; right: 30px; top: 72px; }
  .sign--wide .headline__main { font-size: 46px; }
  .sign--wide .headline__sub { font-size: 25px; }
  .sign--wide .partner-band { height: 110px; }
  .sign--wide .partner-band__label { left: 40px; top: 16px; font-size: 16px; }
  .sign--wide .partner--north { left: 40px; top: 48px; font-size: 30px; }
  .sign--wide .partner--quad { left: 340px; top: 46px; font-size: 30px; gap: 12px; }
  .sign--wide .partner__square { width: 38px; height: 38px; }
  .sign--wide .partner-band__web { right: 40px; top: 54px; font-size: 20px; }
</style>
</head>
<body>
<main class="canvas">

  <section class="sign sign--square" aria-label="Square billboard sign, 2.74 by 2.74 metres">
    <div class="brand">
      <span class="brand__dot"></span>
      <span class="brand__name">BRIGHTWAVE<br>INSIGHTS</span>
    </div>
    <div class="headline">
      <p class="headline__main">AWARD WINNING<br>DATA ANALYTICS</p>
      <p class="headline__sub">IMPLEMENTATION PARTNER</p>
    </div>
    <footer class="partner-band">
      <p class="partner-band__label">PROUDLY PARTNERING WITH</p>
      <p class="partner partner--north">NORTHGATE</p>
      <p class="partner partner--quad"><span class="partner__square"></span>Quadrant</p>
      <p class="partner-band__web">WWW.BRIGHTWAVEINSIGHTS.IE</p>
    </footer>
  </section>

  <section class="sign sign--wide" aria-label="Wide billboard sign, 3 by 1 metres">
    <div class="brand">
      <span class="brand__dot"></span>
      <span class="brand__name">BRIGHTWAVE<br>INSIGHTS</span>
    </div>
    <div class="headline">
      <p class="headline__main">AWARD WINNING<br>DATA ANALYTICS</p>
      <p class="headline__sub">IMPLEMENTATION PARTNER</p>
    </div>
    <footer class="partner-band">
      <p class="partner-band__label">PROUDLY PARTNERING WITH</p>
      <p class="partner partner--north">NORTHGATE</p>
      <p class="partner partner--quad"><span class="partner__square"></span>Quadrant</p>
      <p class="partner-band__web">WWW.BRIGHTWAVEINSIGHTS.IE</p>
    </footer>
  </section>

</main>
</body>
</html>
```